Business card, postcard, pocket folder

We are a real estate team and have had a new logo designed. From this, we need the following deliverables:- Business Cards (double-sided)- Just Listed / Just Sold Postcards (double-sided)- Pocket Folder. See logo attached.More work possible for the winning designer.
There are 5 members of the team, so head shots should be easily changed and possible for a group photo might be a good idea for the pocket folder but not 100% neccessary.
Target Market(s)
Real estate
Industry/Entity Type
Real Estate
Font styles to use
Serif
Sans Serif
Requirements
Must have
- Business cards and postcards must have a head shot on them.

```html
<!DOCTYPE html>
<html lang="en">
<head>
<meta charset="utf-8">
<title>Corvane Group — Business Card</title>
<link href="https://fonts.googleapis.com/css2?family=Work+Sans:wght@400;500;600&display=swap" rel="stylesheet">
<style>
  :root {
    --backdrop: #151515;
    --card: #262626;
    --card-edge: #2e2e2e;
    --brand-blue: #2d48b8;
    --silver: #c9c9c9;
    --text-light: #f2f2f2;
    --headshot-top: #4a4f5c;
    --headshot-bottom: #33363e;
  }
  * { margin: 0; padding: 0; box-sizing: border-box; }
  html, body {
    width: 1200px; height: 900px; overflow: hidden;
    background: var(--backdrop);
    font-family: "Work Sans", Arial, sans-serif;
  }
  .sheet {
    width: 1200px; height: 900px;
    display: flex; flex-direction: column; align-items: center; justify-content: center;
    gap: 40px;
  }
  .card {
    width: 660px; height: 378px;
    background: linear-gradient(135deg, var(--card-edge), var(--card));
    position: relative;
    box-shadow: 0 12px 30px rgba(0,0,0,.55);
  }
  .card--front { display: flex; align-items: center; justify-content: center; }
  .wordmark {
    display: flex; align-items: center; gap: 12px;
    font-weight: 600; letter-spacing: -0.5px; white-space: nowrap;
  }
  .wordmark__square { width: 16px; height: 16px; flex: none; }
  .card--front .wordmark { color: var(--silver); font-size: 46px; }
  .card--front .wordmark__square { background: var(--silver); width: 18px; height: 18px; }

  .card--back { display: flex; align-items: center; padding: 0 40px; }
  .brand-side { width: 262px; display: flex; justify-content: center; padding-right: 24px; }
  .card--back .wordmark { color: var(--brand-blue); font-size: 31px; }
  .card--back .wordmark__square { background: var(--brand-blue); }
  .divider { width: 2px; height: 260px; background: var(--brand-blue); flex: none; }
  .contact {
    padding-left: 32px; color: var(--text-light);
    font-size: 15px; line-height: 1.5; letter-spacing: .4px;
  }
  .headshot {
    width: 64px; height: 64px; border-radius: 50%;
    background: linear-gradient(180deg, var(--headshot-top), var(--headshot-bottom));
    border: 2px solid var(--brand-blue);
    margin-bottom: 12px;
  }
  .contact__name {
    color: var(--brand-blue); font-size: 21px; font-weight: 500;
    letter-spacing: 2px; text-transform: uppercase; line-height: 1.15;
  }
  .contact__role { font-size: 14px; margin-bottom: 10px; }
  .contact__address { margin-bottom: 6px; }
  .contact__line { display: flex; align-items: center; gap: 8px; }
  .contact__icon { width: 11px; height: 11px; flex: none; }
</style>
</head>
<body>
<main class="sheet">
  <section class="card card--front" aria-label="Card front">
    <div class="wordmark"><span class="wordmark__square"></span>Corvane Group</div>
  </section>

  <section class="card card--back" aria-label="Card back">
    <div class="brand-side">
      <div class="wordmark"><span class="wordmark__square"></span>Corvane Group</div>
    </div>
    <div class="divider"></div>
    <div class="contact">
      <div class="headshot" role="img" aria-label="Agent head shot photo"></div>
      <p class="contact__name">Daniel Reyes</p>
      <p class="contact__role">Director</p>
      <p class="contact__address">58 Lorne Avenue,<br>Westbrook, NZ, 4020</p>
      <p class="contact__line">
        <svg class="contact__icon" viewBox="0 0 12 12" aria-hidden="true"><path d="M3 1 L5 3.5 L4 5 Q5 7.5 7 8 L8.5 7 L11 9 L9.5 11 Q3 10 1 2.5 Z" fill="var(--brand-blue)"/></svg>
        (555) 014-2290
      </p>
      <p class="contact__line">
        <svg class="contact__icon" viewBox="0 0 12 12" aria-hidden="true"><rect x="1" y="2.5" width="10" height="7" fill="none" stroke="var(--brand-blue)" stroke-width="1.2"/><path d="M1 2.5 L6 6.5 L11 2.5" fill="none" stroke="var(--brand-blue)" stroke-width="1.2"/></svg>
        info@corvanegroup.com
      </p>
      <p class="contact__line">
        <svg class="contact__icon" viewBox="0 0 12 12" aria-hidden="true"><circle cx="6" cy="6" r="5" fill="none" stroke="var(--brand-blue)" stroke-width="1.2"/><ellipse cx="6" cy="6" rx="2.2" ry="5" fill="none" stroke="var(--brand-blue)" stroke-width="1"/><path d="M1 6 H11" stroke="var(--brand-blue)" stroke-width="1"/></svg>
        www.corvanegroup.com
      </p>
    </div>
  </section>
</main>
</body>
</html>
```